2 Labels Pet Treat Label Hemp Extract "Dogs and Cats"

We are currently looking for an "easy on the eye" type of pet treat label. Our colors are mostly Black and Gold however, we are open to suggestions. First label is your normal "Hemp Extract Pet Treat". Second label is "Hemp Extract for Pain & Inflammation plus calming" We would like to work with you on inputting the small details. Please use buzzwords such as Veterinary recommended etc. We would like our Logo on there as well if possible. Please make room for Ingredient list as well. A search on google for Pet treats CBD... or in this case "Hemp Extract" that should give you some idea of what we are looking for. I normally use Canva however, if you can show us how to make edits for future use, we would appreciate that.. FYI. It's 30 dog treats in a bag. 5mg of Hemp Extract. Totaling 150mg of Hemp Extract.
The 2 Logos should only be different in color since one is for Pain and Inflamation plus calming. and the other is just hemp extract.

Target Market(s)

Dogs & Cats

Font styles to use
Decorative
Script
Other font styles liked:
• Bebas Nuee

Requirements
Must have
• Must Say Hemp Extract and not CBD. Must have 5mg of Hemp Extract. Must have a few buzz words such as Veterinarian recommended, Must say Grain Free. No Dairy.
• The label needs to be on a 3" x 4.5" Sticker. So essentially the label is just a sticker vs the whole bag.
• The sticker will go a brown kraft bag, but the label for this project will be on a 3" x 4.5" Sticker.
Should not have
• CBD

```html
<!DOCTYPE html>
<html lang="en">
<head>
<meta charset="utf-8">
<title>Hemp Extract Pet Treat Labels</title>
<link rel="stylesheet" href="https://fonts.googleapis.com/css2?family=Bebas+Neue&family=Montserrat:wght@500;600;700;800;900&display=swap">
<style>
  :root {
    --page: #ffffff;
    --label-bg: #e8dea3;
    --label-light: #f2edd3;
    --leaf-tone: #e3d79a;
    --ink: #5b5648;
    --ink-dark: #3c3a31;
    --accent-orange: #f18a22;
    --accent-teal: #1c9ec0;
    --dog-dark: #2b2a28;
    --dog-light: #d9d6cf;
  }
  * { box-sizing: border-box; margin: 0; padding: 0; }
  html, body {
    width: 1200px; height: 965px; overflow: hidden;
    background: var(--page);
    font-family: "Montserrat", sans-serif;
  }
  .canvas { position: relative; width: 1200px; height: 965px; }

  .label {
    position: absolute;
    width: 242px; height: 364px;
    background: var(--label-bg);
    border-radius: 8px;
    overflow: hidden;
    color: var(--ink);
  }
  .label--plain { left: 205px; top: 342px; --accent: var(--accent-orange); }
  .label--calming { left: 738px; top: 347px; --accent: var(--accent-teal); }
  .label--calming::after {
    content: ""; position: absolute; inset: 4px;
    border: 1.5px solid var(--label-light); border-radius: 6px;
    pointer-events: none;
  }

  .label__swoosh { position: absolute; inset: 0; }
  .label__pattern {
    position: absolute; left: 0; top: 0; width: 190px; height: 150px;
    background: radial-gradient(ellipse at 30% 40%, rgba(226,216,150,0.35), rgba(242,237,211,0) 70%);
  }
  .label__leaf {
    position: absolute; left: 30px; top: 110px; width: 170px; height: 180px;
    background: radial-gradient(ellipse at 50% 55%, var(--leaf-tone), rgba(227,215,154,0) 70%);
    border-radius: 50%;
  }

  .brand {
    position: absolute; left: 0; right: 0; top: 38px;
    display: flex; flex-direction: column; align-items: center; gap: 6px;
  }
  .brand__mark { width: 22px; height: 22px; background: var(--ink-dark); }
  .brand__name {
    font-family: "Montserrat", sans-serif; font-weight: 700;
    font-size: 9px; letter-spacing: 2.5px; color: var(--ink-dark);
  }

  .title__kicker {
    position: absolute; left: 23px; top: 110px;
    font-family: "Bebas Neue", sans-serif; font-size: 22px; line-height: 1;
    color: var(--ink); letter-spacing: 0.2px;
  }
  .title__main {
    position: absolute; left: 22px; top: 132px; z-index: 2;
    font-family: "Montserrat", sans-serif; font-weight: 900;
    font-size: 35px; line-height: 36px; letter-spacing: -0.5px;
    color: var(--accent);
    -webkit-text-stroke: 1px #fff; paint-order: stroke fill;
  }

  .dose { position: absolute; left: 23px; top: 220px; color: var(--ink); z-index: 2; }
  .dose__amount { font-weight: 800; font-size: 13px; line-height: 1.2; }
  .dose__note { font-weight: 700; font-size: 11px; line-height: 1.2; }

  .label__photo {
    position: absolute; left: 128px; top: 136px; width: 110px; height: 160px;
    background: linear-gradient(160deg, var(--dog-dark) 0%, #4a4742 55%, var(--dog-light) 100%);
    clip-path: polygon(52% 0%, 100% 0%, 100% 100%, 0% 100%, 0% 46%, 22% 42%, 22% 18%);
    opacity: 0.9;
  }

  .facts {
    position: absolute; left: 32px; top: 299px; width: 178px; height: 50px;
    border: 1.2px solid var(--ink); border-radius: 7px;
    display: flex; align-items: stretch; color: var(--ink-dark);
  }
  .facts__count {
    width: 42px; display: flex; align-items: center; justify-content: center;
    font-weight: 800; font-size: 11px; border-right: 1.2px solid var(--ink);
  }
  .facts__count small { font-size: 7px; }
  .facts__free {
    width: 52px; display: flex; flex-direction: column; justify-content: center; align-items: center;
    border-right: 1.2px solid var(--ink); line-height: 1;
  }
  .facts__free span { font-size: 6px; font-weight: 700; }
  .facts__free strong { font-size: 10px; font-weight: 800; margin-bottom: 3px; }
  .facts__free strong:last-child { margin-bottom: 0; }
  .facts__meta { flex: 1; display: flex; flex-direction: column; }
  .facts__vet {
    flex: 1; display: flex; flex-direction: column; justify-content: center; align-items: center;
    font-size: 6.3px; font-weight: 800; line-height: 1.1; border-bottom: 1.2px solid var(--ink);
  }
  .facts__weight {
    flex: 1; display: flex; align-items: center; justify-content: center; gap: 4px;
  }
  .facts__weight span { font-size: 5.5px; font-weight: 600; line-height: 1.1; }
  .facts__weight strong { font-size: 12px; font-weight: 800; }
</style>
</head>
<body>
<main class="canvas">

  <section class="label label--plain">
    <svg class="label__swoosh" viewBox="0 0 242 364" aria-hidden="true">
      <path d="M0 0 H200 C110 30 60 120 80 230 C90 270 110 290 120 300 H0 Z" fill="var(--label-light)"/>
    </svg>
    <div class="label__pattern" role="img" aria-label="Scattered paw print pattern"></div>
    <div class="label__leaf" role="img" aria-label="Large faint hemp leaf decoration"></div>
    <div class="brand"><span class="brand__mark"></span><span class="brand__name">STILLWATER</span></div>
    <div class="label__photo" role="img" aria-label="Photo of a playful black and white dog in a play bow"></div>
    <p class="title__kicker">HEMP EXTRACT</p>
    <h1 class="title__main">PET<br>TREAT</h1>
    <div class="dose"><p class="dose__amount">150mg</p><p class="dose__note">of Hemp Extract</p></div>
    <div class="facts">
      <div class="facts__count">30<small>PCS</small></div>
      <div class="facts__free"><span>GRAIN</span><strong>FREE</strong><span>DAIRY</span><strong>FREE</strong></div>
      <div class="facts__meta">
        <div class="facts__vet">VETERINARIAN<br>RECOMMENDED</div>
        <div class="facts__weight"><span>NET<br>WEIGHT</span><strong>150g</strong></div>
      </div>
    </div>
  </section>

  <section class="label label--calming">
    <svg class="label__swoosh" viewBox="0 0 242 364" aria-hidden="true">
      <path d="M0 0 H200 C110 30 60 120 80 230 C90 270 110 290 120 300 H0 Z" fill="var(--label-light)"/>
    </svg>
    <div class="label__pattern" role="img" aria-label="Scattered paw print pattern"></div>
    <div class="label__leaf" role="img" aria-label="Large faint hemp leaf decoration"></div>
    <div class="brand"><span class="brand__mark"></span><span class="brand__name">STILLWATER</span></div>
    <div class="label__photo" role="img" aria-label="Photo of a playful black and white dog in a play bow"></div>
    <p class="title__kicker">HEMP EXTRACT</p>
    <h1 class="title__main">PET<br>TREAT</h1>
    <div class="dose"><p class="dose__amount">150mg</p><p class="dose__note">of Hemp Extract</p></div>
    <div class="facts">
      <div class="facts__count">30<small>PCS</small></div>
      <div class="facts__free"><span>GRAIN</span><strong>FREE</strong><span>DAIRY</span><strong>FREE</strong></div>
      <div class="facts__meta">
        <div class="facts__vet">VETERINARIAN<br>RECOMMENDED</div>
        <div class="facts__weight"><span>NET<br>WEIGHT</span><strong>150g</strong></div>
      </div>
    </div>
  </section>

</main>
</body>
</html>
```